Brinewardsea.com Website design needed!!

We are looking for a website layout to match the attached logo. We specialize in Dive Charters and currently are located in the Virgin Islands off of St. Thomas. Please create a design that is compatible with Bootstrap and have the grid in mind. WE are looking for creative and extremely professional layout design.

Target Market(s)

Scuba Diving, Divers looking for a diving charter in the Virgin Islands.

Number of Pages Required

3 page

Font styles to use
Serif

Requirements
Must have
• Must be Bootstrap friendly.
• Must work with the logo we provided. Colors etc.

```html
<!DOCTYPE html>
<html lang="en">
<head>
<meta charset="utf-8">
<title>Brinewardsea – Learn Scuba Diving</title>
<link href="https://fonts.googleapis.com/css2?family=Courgette&family=Open+Sans:wght@400;600;700&display=swap" rel="stylesheet">
<style>
:root{
  --red:#d8101d;
  --blue:#1f9be6;
  --blue-dark:#1a7fc4;
  --navy:#0b3f7a;
  --deep:#0a2660;
  --ink:#222;
  --muted:#444;
  --grey:#ececec;
  --white:#fff;
}
*{box-sizing:border-box;margin:0;padding:0}
html,body{width:1200px;height:2353px;overflow:hidden}
body{font-family:"Open Sans",Arial,sans-serif;color:var(--ink);background:var(--white);position:relative}
.abs{position:absolute}

/* hero */
.hero{position:absolute;left:0;top:0;width:1200px;height:700px;overflow:hidden}
.hero-art{position:absolute;inset:0;background:
  radial-gradient(ellipse 520px 260px at 50% 28%,rgba(140,218,250,.95) 0%,rgba(140,218,250,0) 100%),
  radial-gradient(circle at 0 0,#123f86 0,rgba(18,63,134,.8) 140px,rgba(18,63,134,0) 330px),
  radial-gradient(circle at 100% 0,#123f86 0,rgba(18,63,134,.8) 120px,rgba(18,63,134,0) 300px),
  linear-gradient(180deg,#3aa9e6 0%,#2a96dc 40%,#1b78c6 62%,#155fb0 100%)}
.hero-reef{position:absolute;left:0;top:320px;width:1200px;height:380px;background:
  radial-gradient(ellipse 260px 120px at 22% 55%,rgba(60,190,200,.55),rgba(60,190,200,0)),
  radial-gradient(ellipse 300px 90px at 55% 30%,rgba(150,210,120,.45),rgba(150,210,120,0)),
  radial-gradient(ellipse 200px 110px at 85% 60%,rgba(220,70,90,.35),rgba(220,70,90,0)),
  linear-gradient(180deg,rgba(26,79,156,0) 0%,#1a4f9c 30%,#0f3578 58%,var(--deep) 100%)}
.hero-edge{position:absolute;left:0;top:560px}
.brand{position:absolute;left:0;width:1200px;top:70px;text-align:center}
.brand-name{display:inline-flex;align-items:center;gap:10px;font-family:"Courgette",cursive;font-size:40px;color:var(--white)}
.brand-name .dot{width:16px;height:16px;border-radius:50%;background:var(--red)}
.brand-sub{display:block;font-size:14px;font-weight:700;letter-spacing:2px;color:var(--white);margin-top:2px}
.menu-btn{position:absolute;left:1055px;top:36px;width:52px;height:52px;border-radius:14px;background:var(--red);border:2px solid #fff}
.menu-btn span{position:absolute;left:12px;width:28px;height:3px;background:#fff;border-radius:2px}
.hero-kicker{position:absolute;left:0;width:1200px;top:205px;text-align:center;font-family:"Courgette",cursive;font-size:52px;color:var(--white)}
.hero-title{position:absolute;left:0;width:1200px;top:262px;text-align:center;font-size:62px;font-weight:700;color:var(--white);letter-spacing:1px}
.hero-arrow{position:absolute;top:267px}

/* side tab */
.help-tab{position:absolute;left:1172px;top:243px;width:28px;height:141px;background:#fff;border:1px solid #ccc;border-right:0;display:flex;align-items:center;justify-content:center}
.help-tab span{writing-mode:vertical-rl;transform:rotate(180deg);font-size:13px;font-weight:700;white-space:nowrap;color:#111}
.help-q{position:absolute;left:1172px;top:384px;width:28px;height:40px;background:#111;color:#fff;font-weight:700;text-align:center;line-height:40px}
.social{position:absolute;left:1172px;width:28px;height:28px}

/* intro */
.intro-art-left{position:absolute;left:0;top:863px;width:110px;height:203px;background:linear-gradient(160deg,#f0c9a0,#c23030 55%,#1c2a44);border-radius:40px 60px 0 0}
.intro-art-right{position:absolute;left:1051px;top:808px;width:149px;height:258px;background:linear-gradient(200deg,#e2242f,#f6d2b2 50%,#2a3444);border-radius:60px 0 0 40px}
.sec-title{font-family:"Courgette",cursive;color:var(--red);font-size:26px;font-weight:400;line-height:1.2}
.sec-sub{font-size:15.5px;color:var(--ink);line-height:1.2}
.story{left:117px;top:732px;width:428px}
.story-text{font-size:12.5px;line-height:17.5px;color:var(--muted);margin-top:26px}
.btn-outline{display:inline-block;margin-top:20px;padding:8px 14px;border:2px solid #57a6d8;border-radius:10px;color:var(--blue-dark);font-weight:600;font-size:14px}
.why{left:658px;top:732px;width:400px}
.feature{position:relative;padding-left:70px;margin-top:19px}
.why .sec-sub + .feature{margin-top:22px}
.feature svg{position:absolute;left:0;top:2px}
.feature h3{font-size:15px;font-weight:700;line-height:19px}
.feature p{font-size:13.5px;line-height:17px;color:var(--muted);max-width:272px}

/* tiles */
.tile{position:absolute;overflow:hidden;color:var(--white)}
.tile .photo{position:absolute;inset:0}
.tile .shade{position:absolute;inset:0;background:linear-gradient(180deg,rgba(0,0,0,0) 35%,rgba(0,0,0,.7) 100%)}
.tile .body{position:absolute;left:24px;right:24px;bottom:26px}
.tile.wide .body{left:94px}
.tile h3{font-size:21px;font-weight:600;text-transform:uppercase;line-height:1.25}
.tile p{font-size:13.5px;line-height:18px;color:#ddd;margin-top:6px;max-width:275px}
.tile.wide p{max-width:300px}
.tile a{display:block;color:#ff2a2a;font-size:12px;margin-top:10px;text-decoration:none}

/* subscribe */
.subscribe{position:absolute;left:0;top:1577px;width:1200px;height:125px;background:var(--blue)}
.subscribe h2{position:absolute;left:97px;top:28px;font-size:23px;font-weight:700;color:#111}
.subscribe .lead{position:absolute;left:97px;top:59px;font-size:20px;color:#0d3b66}
.email{position:absolute;left:534px;top:33px;width:302px;height:44px;background:#fff;font-size:12.5px;color:#777;padding:13px 8px}
.email-go{position:absolute;left:836px;top:33px;width:40px;height:44px;background:#1577c2}
.btn-ghost{position:absolute;left:895px;top:33px;width:210px;height:44px;border:1.5px solid #fff;color:#fff;font-size:15px;text-align:center;line-height:41px}

/* events */
.events{position:absolute;left:0;top:1702px;width:1200px;height:487px;background:var(--blue-dark)}
.events-paper{position:absolute;left:70px;top:10px;width:1060px;height:477px;background:#fff;border-radius:60px 90px 0 0}
.events-title{position:absolute;left:0;width:1200px;top:22px;text-align:center;font-family:"Courgette",cursive;font-size:25px;font-weight:400;color:#1e82c8}
.events-rule{position:absolute;left:316px;top:66px;width:568px;height:2px;background:#bbb}
.card{position:absolute;top:107px;width:236px;height:272px;background:#fff;border:1px solid #ccc}
.card .photo{height:106px;background:linear-gradient(180deg,#2e84c8,#3ca0a0 60%,#c9a23e)}
.card h4{height:34px;background:var(--red);color:#fff;font-size:15.5px;font-weight:600;padding:6px 14px}
.card .date{font-size:12.5px;font-weight:700;color:#1565c0;padding:6px 8px 2px 8px;display:flex;gap:8px;align-items:center}
.card ul{list-style:none;padding:0 8px}
.card li{font-size:12px;line-height:17.5px;color:#222;display:flex;gap:8px;align-items:center}
.card li::before{content:"★";color:#1565c0;font-size:12px}
.card .more{position:absolute;left:-19px;bottom:-21px;width:112px;height:42px;background:var(--red);color:#fff;font-size:12px;padding:13px 0 0 14px;clip-path:polygon(0 0,100% 0,100% 60%,85% 100%,0 100%)}
.dots{position:absolute;top:446px;left:0;width:1200px;display:flex;justify-content:center;gap:14px}
.dots span{width:15px;height:15px;border-radius:50%;border:2px solid #1f82c8}
.dots span.on{background:#1f82c8}
.deco{position:absolute}

/* testimonials */
.testimonials{position:absolute;left:0;top:2189px;width:1200px;height:125px;background:var(--grey)}
.testimonials h2{position:absolute;left:94px;top:26px;font-family:"Courgette",cursive;font-size:27px;font-weight:400;color:#111}
.testimonials .tag{position:absolute;left:94px;top:72px;width:150px;font-size:12.5px;line-height:15px;color:var(--muted)}
.testimonials .rule{position:absolute;left:278px;top:16px;width:1px;height:92px;background:#777}
.avatar{position:absolute;left:308px;top:26px;width:74px;height:74px;border-radius:50%;background:#c9c9c9;border:3px solid #fff}
.testimonials blockquote{position:absolute;left:415px;top:26px;width:672px;font-size:13.5px;line-height:18px;color:#222}

/* footer */
.footer{position:absolute;left:0;top:2314px;width:1200px;height:39px;background:var(--blue)}
.footer nav{position:absolute;left:93px;top:11px;display:flex;gap:19px}
.footer nav a{color:#0d2d55;font-size:12.5px;text-decoration:none}
.footer nav a.active{color:#fff;border-bottom:2px solid #fff}
.footer small{position:absolute;right:95px;top:12px;font-size:12px;color:#0d2d55}
</style>
</head>
<body>

<header class="hero">
  <div class="hero-art" role="img" aria-label="Illustrated underwater reef scene with fish shoal, corals and divers in silhouette"></div>
  <div class="hero-reef"></div>
  <svg class="hero-edge" width="1200" height="140" viewBox="0 0 1200 140" aria-hidden="true">
    <path d="M0 70 C60 40 110 95 170 70 C230 45 270 100 340 78 C410 56 440 110 520 90 C600 70 640 40 700 62 C760 84 800 110 870 84 C940 58 990 100 1050 80 C1110 60 1160 95 1200 72 L1200 140 L0 140 Z" fill="#fff"/>
  </svg>
  <div class="brand">
    <span class="brand-name"><span class="dot"></span>Brinewardsea</span>
    <span class="brand-sub">ST. THOMAS</span>
  </div>
  <div class="menu-btn" aria-label="Menu"><span style="top:16px"></span><span style="top:24px"></span><span style="top:32px"></span></div>
  <div class="hero-kicker">Live the moment</div>
  <h1 class="hero-title">LEARN SCUBA DIVING</h1>
  <svg class="hero-arrow" style="left:122px" width="30" height="56" viewBox="0 0 30 56"><polyline points="26,2 4,28 26,54" fill="none" stroke="rgba(255,255,255,.6)" stroke-width="2"/></svg>
  <svg class="hero-arrow" style="left:1050px" width="30" height="56" viewBox="0 0 30 56"><polyline points="4,2 26,28 4,54" fill="none" stroke="rgba(255,255,255,.6)" stroke-width="2"/></svg>
</header>

<aside>
  <div class="help-tab"><span>May I Help You !</span></div>
  <div class="help-q">?</div>
  <div class="social" style="top:436px;background:#3b5998"></div>
  <div class="social" style="top:465px;background:#29a9e1"></div>
  <div class="social" style="top:494px;background:#0e76a8"></div>
  <div class="social" style="top:523px;background:#d4232b"></div>
  <div class="social" style="top:552px;background:#cb2027"></div>
</aside>

<section>
  <div class="intro-art-left" role="img" aria-label="Illustrated diver with mask and regulator"></div>
  <div class="intro-art-right" role="img" aria-label="Illustrated diver legs with red fins"></div>

  <div class="abs story">
    <h2 class="sec-title">Discover our Story</h2>
    <p class="sec-sub">We are at the Virgin Islands off of St. Thomas</p>
    <p class="story-text">Lorem ipsum dolor sit amet, consectetuer adipiscing elit, sed diam nonummy nibh euismod tincidunt ut laoreet dolore magna aliquam erat volutpat. Ut wisi enim ad minim veniam, quis nostrud exerci tation ullamcorper suscipit lobortis nisl ut aliquip ex ea commodo consequat. Duis autem vel eum iriure dolor in hendrerit in vulputate velit esse molestie consequat, vel illum dolore eu feugiat nulla. uscipit lobortis nisl ut aliquip ex ea commodo consequat. Duis autem vel eum iriure dolor.</p>
    <span class="btn-outline">EXPLORE OUR STORY</span>
  </div>

  <div class="abs why">
    <h2 class="sec-title">Why choose us</h2>
    <p class="sec-sub">Gather experiences Like Never Before In Your Life</p>
    <div class="feature">
      <svg width="42" height="42" viewBox="0 0 42 42"><circle cx="21" cy="21" r="18" fill="none" stroke="#1f82c8" stroke-width="3"/><text x="21" y="29" text-anchor="middle" font-family="Open Sans, sans-serif" font-size="22" font-weight="700" fill="#1f82c8">$</text></svg>
      <h3>COMPETITIVE PRICE</h3>
      <p>Lorem ipsum dolor sit amet, consectetur adipiscing elit.</p>
    </div>
    <div class="feature">
      <svg width="42" height="42" viewBox="0 0 42 42"><circle cx="21" cy="21" r="17" fill="none" stroke="#1f82c8" stroke-width="8"/><circle cx="21" cy="21" r="17" fill="none" stroke="#fff" stroke-width="8" stroke-dasharray="8 18.7"/><circle cx="21" cy="21" r="21" fill="none" stroke="#1f82c8" stroke-width="1"/></svg>
      <h3>SAFE &amp; FUN</h3>
      <p>Lorem ipsum dolor sit amet, consectetur adipiscing elit.</p>
    </div>
    <div class="feature">
      <svg width="42" height="42" viewBox="0 0 42 42"><rect x="3" y="12" width="30" height="20" rx="9" fill="none" stroke="#1f82c8" stroke-width="3"/><path d="M36 4 V30 q0 8 -8 8" fill="none" stroke="#1f82c8" stroke-width="3"/></svg>
      <h3>KIDS PROGRAMS</h3>
      <p>Lorem ipsum dolor sit amet, consectetur adipiscing elit.</p>
    </div>
  </div>
</section>

<section>
  <article class="tile wide" style="left:0;top:1067px;width:421px;height:510px">
    <div class="photo" role="img" aria-label="Photo of two divers in masks underwater" style="background:linear-gradient(160deg,#1ea2d8,#0c6a9c 50%,#062c48)"></div>
    <div class="shade"></div>
    <div class="body"><h3>Suba Diving</h3><p>Lorem ipsum dolor sit amet, consectetuer adipiscing elit, sed diam nonummy .</p><a>Explore Here</a></div>
  </article>
  <article class="tile" style="left:424px;top:1067px;width:398px;height:251px">
    <div class="photo" role="img" aria-label="Photo of divers at the surface of the sea" style="background:linear-gradient(180deg,#c5d6e6,#7c97b0 45%,#2c3e52)"></div>
    <div class="shade"></div>
    <div class="body"><h3>Latest Campaigns</h3><p>Lorem ipsum dolor sit amet, consectetuer adipiscing elit euismod</p></div>
  </article>
  <article class="tile" style="left:825px;top:1067px;width:375px;height:251px">
    <div class="photo" role="img" aria-label="Photo of a happy group on a dive charter boat" style="background:linear-gradient(180deg,#2e4f8a,#8a98a8 45%,#2a2a2a)"></div>
    <div class="shade"></div>
    <div class="body"><h3>We Provide Diving<br>Charter For Driver</h3><p>Lorem ipsum dolor sit amet,diam nonummy nibh euismod</p><a>Explore Here</a></div>
  </article>
  <article class="tile" style="left:424px;top:1322px;width:398px;height:255px">
    <div class="photo" role="img" aria-label="Photo of a diver with camera in an underwater cave" style="background:radial-gradient(circle at 50% 40%,#3aa0d8,#10304a 70%,#6a1a2a)"></div>
    <div class="shade"></div>
    <svg class="abs" style="left:163px;top:60px" width="72" height="72" viewBox="0 0 72 72"><circle cx="36" cy="36" r="35" fill="#d8101d"/><polygon points="28,20 28,52 54,36" fill="#fff"/></svg>
    <div class="body"><h3>Latest Video</h3><p>Lorem ipsum dolor sit amet, consectetuer adipiscing elit euismod</p></div>
  </article>
  <article class="tile" style="left:825px;top:1322px;width:375px;height:255px">
    <div class="photo" role="img" aria-label="Photo of a diver over a coral reef" style="background:linear-gradient(180deg,#1f78c0,#1a5a8c 55%,#0b2c48)"></div>
    <div class="shade"></div>
    <div class="body"><h3>Gallery</h3><p>Lorem ipsum dolor sit amet, consectetuer sed diam nonummy mod</p></div>
  </article>
</section>

<section class="subscribe">
  <h2>Stay up to date! Subscribe to us!</h2>
  <p class="lead">Find what's going on!</p>
  <div class="email">Enter your email Id</div>
  <div class="email-go"><svg width="40" height="44" viewBox="0 0 40 44"><polyline points="16,14 24,22 16,30" fill="none" stroke="#fff" stroke-width="3"/></svg></div>
  <div class="btn-ghost">EXPLORE OUR GALLERY</div>
</section>

<section class="events">
  <div class="events-paper"></div>
  <div class="deco" role="img" aria-label="Illustrated red air tank" style="left:80px;top:55px;width:50px;height:100px;background:#e02020;border-radius:22px 22px 8px 8px;transform:rotate(30deg)"></div>
  <div class="deco" role="img" aria-label="Illustrated snorkel mask" style="left:960px;top:10px;width:150px;height:50px;background:linear-gradient(90deg,#f2c12e,#e02020);border-radius:20px"></div>
  <div class="deco" role="img" aria-label="Illustrated pair of red fins" style="left:40px;top:370px;width:140px;height:90px;background:linear-gradient(135deg,#e02020,#f08080);border-radius:50px 20px 40px 20px"></div>
  <div class="deco" role="img" aria-label="Illustrated dive gauge" style="left:1045px;top:380px;width:60px;height:90px;background:#b8c4cc;border-radius:30px 30px 10px 10px"></div>

  <h2 class="events-title">Our upcoming events</h2>
  <div class="events-rule"></div>

  <div class="card" style="left:229px">
    <div class="photo" role="img" aria-label="Photo of a diver by a coral reef"></div>
    <h4>Socorro Islands Tour</h4>
    <div class="date"><svg width="14" height="14" viewBox="0 0 14 14"><rect x="1" y="2" width="12" height="11" fill="none" stroke="#666"/><line x1="1" y1="5" x2="13" y2="5" stroke="#666"/></svg>09 Mar 2015 - 19 Mar 2015</div>
    <ul><li>All Transfers</li><li>10 Nights Accommodation</li><li>Breakfast &amp; Local Drinks</li><li>Marine Park Fees</li></ul>
    <div class="more">LEARN MORE</div>
  </div>
  <div class="card" style="left:491px">
    <div class="photo" role="img" aria-label="Photo of a diver by a coral reef"></div>
    <h4>Socorro Islands Tour</h4>
    <div class="date"><svg width="14" height="14" viewBox="0 0 14 14"><rect x="1" y="2" width="12" height="11" fill="none" stroke="#666"/><line x1="1" y1="5" x2="13" y2="5" stroke="#666"/></svg>09 Mar 2015 - 19 Mar 2015</div>
    <ul><li>All Transfers</li><li>10 Nights Accommodation</li><li>Breakfast &amp; Local Drinks</li><li>Marine Park Fees</li></ul>
    <div class="more">LEARN MORE</div>
  </div>
  <div class="card" style="left:764px">
    <div class="photo" role="img" aria-label="Photo of a diver by a coral reef"></div>
    <h4>Socorro Islands Tour</h4>
    <div class="date"><svg width="14" height="14" viewBox="0 0 14 14"><rect x="1" y="2" width="12" height="11" fill="none" stroke="#666"/><line x1="1" y1="5" x2="13" y2="5" stroke="#666"/></svg>09 Mar 2015 - 19 Mar 2015</div>
    <ul><li>All Transfers</li><li>10 Nights Accommodation</li><li>Breakfast &amp; Local Drinks</li><li>Marine Park Fees</li></ul>
    <div class="more">LEARN MORE</div>
  </div>

  <div class="dots"><span></span><span class="on"></span><span></span></div>
</section>

<section class="testimonials">
  <h2>Testimonials</h2>
  <p class="tag">Reputation is everything for us</p>
  <div class="rule"></div>
  <div class="avatar" role="img" aria-label="Portrait photo of a customer"></div>
  <blockquote>Lorem ipsum dolor sit amet, consectetuer adipiscing elit, sed diam nonummy nibh euismod tincidunt ut laoreet dolore magna aliquam erat volutpat. Ut wisi enim ad minim veniam, quis nostrud exerci tation ullamcorper suscipit lobortis nisl ut aliquip ex ea commodo consequat</blockquote>
</section>

<footer class="footer">
  <nav><a class="active">Home</a><a>About Us</a><a>Scuba Diving</a><a>Courses</a><a>Gallery</a><a>Price List</a><a>Contact</a></nav>
  <small>Copyright 2016 ©Brinewardsea</small>
</footer>

</body>
</html>
```